Bref créative
Stationery for an intellectual property right service provider
ZENOLT
Simple
Tarek Baduri
CEO
Lövbergsvägen 7
164 52 Norrvik
Sweden
tarek.baduri@zenolt.eu
www.zenolt.eu

```html
<!DOCTYPE html>
<html lang="en">
<head>
<meta charset="utf-8">
<title>ZENOLT Stationery</title>
<link rel="stylesheet" href="https://fonts.googleapis.com/css2?family=Cinzel:wght@400;600&family=Open+Sans:wght@400;600&display=swap">
<style>
:root{
  --bg-dark:#1b1b1b;
  --bg-mid:#2c2c2c;
  --paper:#ffffff;
  --paper-shade:#e9e9e9;
  --brand-red:#b3141b;
  --brand-red-dark:#7e0c10;
  --ink:#3a3a3a;
  --ink-soft:#8a8a8a;
  --steel:#5a5a5a;
  --steel-dark:#2a2a2a;
}
*{margin:0;padding:0;box-sizing:border-box}
html,body{width:1200px;height:382px;overflow:hidden}
body{background:radial-gradient(ellipse at 55% 40%,var(--bg-mid),var(--bg-dark) 75%);font-family:"Open Sans",sans-serif;position:relative}
.brand{font-family:"Cinzel",serif;font-weight:600;letter-spacing:1px;color:var(--brand-red);white-space:nowrap}
.piece{position:absolute;box-shadow:0 3px 8px rgba(0,0,0,.55)}

/* presentation logo */
.hero-logo{position:absolute;left:36px;top:140px;display:flex;align-items:center;gap:12px}
.hero-logo .brand{font-size:34px;color:#c9c9c9}
.hero-logo .tagline{border-left:1px solid #6a6a6a;padding-left:8px;font-size:7px;line-height:10px;color:#9a9a9a}
.concept-label{position:absolute;left:44px;top:205px;font-family:"Cinzel",serif;font-size:10px;color:#9a9a9a}

/* business cards */
.card{width:104px;height:62px;display:flex;align-items:center;justify-content:center;flex-direction:column}
.card .brand{font-size:15px}
.card small{font-size:4px;color:var(--ink-soft);margin-top:2px}
.card-steel{left:12px;top:233px;background:linear-gradient(135deg,#8a8a8a,var(--steel-dark) 70%)}
.card-steel .brand{color:#eee}
.card-front{left:124px;top:233px;background:var(--paper);align-items:flex-start;justify-content:flex-start;padding:8px}
.card-front .brand{font-size:13px}
.card-front .band{position:absolute;left:0;right:0;bottom:8px;height:5px;background:linear-gradient(90deg,var(--steel),#bbb)}
.card-red{left:12px;top:307px;background:linear-gradient(135deg,var(--brand-red),var(--brand-red-dark))}
.card-red .brand{color:#fff}
.card-red small{color:#f2c6c6}
.card-white{left:124px;top:307px;background:var(--paper)}
.card-white .contact{font-size:4px;line-height:5px;color:var(--ink);text-align:center;margin-top:4px}

/* letterheads */
.letterhead{width:252px;height:360px;top:12px;background:var(--paper)}
.letterhead-1{left:331px}
.letterhead-2{left:600px}
.letterhead header{position:absolute;left:54px;top:12px;display:flex;gap:8px;align-items:center}
.letterhead header .brand{font-size:17px}
.letterhead .address{font-size:4px;line-height:5px;color:var(--ink-soft);border-left:1px solid #ccc;padding-left:4px}
.letterhead .contact-top{position:absolute;right:12px;top:14px;font-size:4px;line-height:5px;color:var(--ink-soft);text-align:right}
.letterhead footer{position:absolute;left:0;right:0;bottom:0;height:10px;background:linear-gradient(90deg,var(--paper-shade),#bdbdbd,var(--paper-shade));font-size:4px;line-height:10px;text-align:center;color:var(--ink)}

/* envelopes */
.envelope{left:871px;width:317px;background:var(--paper);overflow:hidden}
.envelope svg{position:absolute;inset:0;width:100%;height:100%}
.envelope .brand{position:absolute;font-size:12px}
.env-red{top:12px;height:100px}
.env-steel{top:120px;height:106px}
.env-white{top:236px;height:74px}
.env-plain{top:318px;height:54px}
</style>
</head>
<body>

<div class="hero-logo">
  <span class="brand">ZENOLT</span>
  <span class="tagline">Intellectual<br>Property<br>Rights</span>
</div>
<p class="concept-label">Stationary Concepts</p>

<div class="piece card card-steel"><span class="brand">ZENOLT</span><small>www.zenolt.eu</small></div>
<div class="piece card card-front"><span class="brand">ZENOLT</span><div class="band"></div></div>
<div class="piece card card-red"><span class="brand">ZENOLT</span><small>www.zenolt.eu</small></div>
<div class="piece card card-white">
  <span class="brand" style="font-size:9px">Tarek Baduri</span>
  <div class="contact">CEO<br>Lövbergsvägen 7, 164 52 Norrvik, Sweden<br>tarek.baduri@zenolt.eu</div>
</div>

<section class="piece letterhead letterhead-1">
  <header><span class="brand">ZENOLT</span><span class="address">Lövbergsvägen 7<br>164 52 Norrvik<br>Sweden</span></header>
  <div class="contact-top">tarek.baduri@zenolt.eu<br>www.zenolt.eu</div>
  <footer>Lövbergsvägen 7 · 164 52 Norrvik · www.zenolt.eu</footer>
</section>
<section class="piece letterhead letterhead-2">
  <header><span class="brand">ZENOLT</span><span class="address">Lövbergsvägen 7<br>164 52 Norrvik<br>Sweden</span></header>
  <div class="contact-top">tarek.baduri@zenolt.eu<br>www.zenolt.eu</div>
  <footer>Lövbergsvägen 7 · 164 52 Norrvik · www.zenolt.eu</footer>
</section>

<div class="piece envelope env-red">
  <svg viewBox="0 0 317 100" preserveAspectRatio="none"><path d="M0 0H317V38L158 70L0 38Z" fill="#b3141b"/><path d="M0 38L158 70L317 38" fill="none" stroke="#7e0c10" stroke-width="1"/></svg>
  <span class="brand" style="left:140px;top:76px;font-size:9px">ZENOLT</span>
</div>
<div class="piece envelope env-steel">
  <svg viewBox="0 0 317 106" preserveAspectRatio="none"><defs><linearGradient id="steel" x1="0" y1="0" x2="1" y2="0"><stop offset="0" stop-color="#2a2a2a"/><stop offset=".5" stop-color="#9a9a9a"/><stop offset="1" stop-color="#2a2a2a"/></linearGradient></defs><path d="M0 0H317V40L158 72L0 40Z" fill="url(#steel)"/></svg>
  <span class="brand" style="left:140px;top:80px;font-size:9px">ZENOLT</span>
</div>
<div class="piece envelope env-white">
  <svg viewBox="0 0 317 74" preserveAspectRatio="none"><path d="M0 0L158 36L317 0" fill="none" stroke="#d5d5d5"/></svg>
  <span class="brand" style="left:10px;top:8px">ZENOLT</span>
</div>
<div class="piece envelope env-plain">
  <span class="brand" style="left:10px;top:8px">ZENOLT</span>
</div>

</body>
</html>
```